Business Management System Providor Needs Upscale Business Card Design

We provide an online Claims Management System to the Insurance Industry called Meridel Casework Suite. Although our core offering is claims management, our system provides full business management features including reporting, invoicing, business trend analysis, etc..
We have a worldwide client base and our system has become known for its reliability, rich feature set, and intuitive design. This being the case we would like our cards to maintain a high level of professionalism. We have a tendency to lean toward a corporate look and feel and we would like to maintain that image.
Current Site: www.merideldesk-example.com
Target Market(s)
Big Business, Insurance Professionals, Corporate Organizations
Industry/Entity Type
Business Management
Look and feel
Each slider illustrates characteristics of the customer's brand and the style your logo design should communicate.

```html
<!DOCTYPE html>
<html lang="en">
<head>
<meta charset="utf-8">
<title>Meridel Casework Suite — Business Card</title>
<link rel="stylesheet" href="https://fonts.googleapis.com/css2?family=Arimo:wght@400;700&family=Lato:wght@400;700&display=swap">
<style>
  :root {
    --bg: #2b2b2b;
    --card: #f7f7f7;
    --card-shade: #e9e9e9;
    --blue: #1d4f86;
    --blue-dark: #163d68;
    --grey-stripe: #a9abae;
    --text-grey: #555a60;
    --white: #ffffff;
  }
  * { box-sizing: border-box; margin: 0; padding: 0; }
  html, body { width: 1200px; height: 997px; overflow: hidden; }
  body {
    background: var(--bg);
    font-family: "Arimo", Arial, sans-serif;
    display: flex;
    align-items: center;
    justify-content: center;
    gap: 48px;
  }
  .card {
    position: relative;
    width: 540px;
    height: 309px;
    border-radius: 16px;
    overflow: hidden;
    background: linear-gradient(180deg, var(--white), var(--card) 60%, var(--card-shade));
  }

  /* Front */
  .card-front .top-band {
    position: absolute; left: 0; right: 0; top: 0; height: 34px;
    background: var(--blue);
  }
  .card-front .top-band::after {
    content: ""; position: absolute; left: 0; right: 0; bottom: -6px; height: 6px;
    background: var(--grey-stripe);
  }
  .brand {
    display: flex; align-items: center; gap: 16px;
    color: var(--blue);
    font-weight: 700;
  }
  .brand-mark {
    flex: none;
    background: var(--blue);
    border-radius: 14px;
  }
  .card-front .brand {
    position: absolute; left: 0; right: 0; top: 130px;
    justify-content: center;
    font-size: 34px;
  }
  .card-front .brand-mark { width: 62px; height: 62px; }

  /* Back */
  .card-back .brand {
    position: absolute; left: 28px; top: 104px;
    width: 250px;
    font-size: 24px; line-height: 1.1; gap: 12px;
  }
  .card-back .brand-mark { width: 54px; height: 54px; border-radius: 12px; }
  .divider {
    position: absolute; left: 292px; top: 22px; width: 2px; height: 188px;
    background: linear-gradient(180deg, transparent, var(--blue) 30%, var(--blue) 70%, transparent);
  }
  .person {
    position: absolute; left: 312px; right: 20px; top: 22px;
    text-align: center;
  }
  .person-name { color: var(--blue); font-size: 17px; font-weight: 700; letter-spacing: 0.5px; }
  .person-title { color: #333; font-size: 11px; font-weight: 700; margin-top: 4px; line-height: 1.25; }
  .contact-list {
    position: absolute; left: 312px; top: 92px;
    list-style: none;
    font-family: "Lato", Arial, sans-serif;
    font-size: 11.5px; color: var(--text-grey);
  }
  .contact-list li { display: flex; align-items: flex-start; gap: 8px; margin-bottom: 8px; line-height: 1.35; }
  .contact-list svg { flex: none; width: 18px; height: 18px; }
  .bottom-band {
    position: absolute; left: 0; right: 0; bottom: 0; height: 76px;
    background: var(--blue);
    display: flex; align-items: center; justify-content: center;
  }
  .bottom-band::before {
    content: ""; position: absolute; left: 0; right: 0; top: -10px; height: 10px;
    background: var(--grey-stripe);
  }
  .website {
    color: var(--white); font-family: "Lato", Arial, sans-serif;
    font-size: 14px; letter-spacing: 3px;
  }
</style>
</head>
<body>

  <section class="card card-front" aria-label="Card front">
    <div class="top-band"></div>
    <div class="brand">
      <span class="brand-mark"></span>
      <span class="brand-name">Meridel Casework Suite</span>
    </div>
  </section>

  <section class="card card-back" aria-label="Card back">
    <div class="brand">
      <span class="brand-mark"></span>
      <span class="brand-name">Meridel Casework Suite</span>
    </div>
    <div class="divider"></div>
    <div class="person">
      <p class="person-name">DANA WHITLOW</p>
      <p class="person-title">DIRECTOR OF<br>SOFTWARE DEVELOPMENT</p>
    </div>
    <ul class="contact-list">
      <li>
        <svg viewBox="0 0 18 18" aria-hidden="true"><circle cx="9" cy="9" r="9" fill="#1d4f86"/><path d="M6 5l2 0 1 2.5-1.2 1a5 5 0 0 0 2.7 2.7l1-1.2 2.5 1v2a1 1 0 0 1-1 1A8 8 0 0 1 5 6a1 1 0 0 1 1-1z" fill="#fff"/></svg>
        <span>555-014-2290 x214</span>
      </li>
      <li>
        <svg viewBox="0 0 18 18" aria-hidden="true"><circle cx="9" cy="9" r="9" fill="#1d4f86"/><rect x="4.5" y="6" width="9" height="6.5" fill="none" stroke="#fff" stroke-width="1.2"/><path d="M4.5 6l4.5 3.5L13.5 6" fill="none" stroke="#fff" stroke-width="1.2"/></svg>
        <span>555-019-7731</span>
      </li>
      <li>
        <svg viewBox="0 0 18 18" aria-hidden="true"><circle cx="9" cy="9" r="9" fill="#1d4f86"/><path d="M7.5 10.5l3-3M8 6.5l1-1a2 2 0 0 1 2.8 2.8l-1 1M10 11.5l-1 1a2 2 0 0 1-2.8-2.8l1-1" fill="none" stroke="#fff" stroke-width="1.3" stroke-linecap="round"/></svg>
        <span>dwhitlow@merideldesk-example.com</span>
      </li>
      <li>
        <svg viewBox="0 0 18 18" aria-hidden="true"><circle cx="9" cy="9" r="9" fill="#1d4f86"/><path d="M9 14s-3.5-3.6-3.5-6a3.5 3.5 0 0 1 7 0c0 2.4-3.5 6-3.5 6z" fill="#fff"/><circle cx="9" cy="8" r="1.3" fill="#1d4f86"/></svg>
        <span>1180 Harborline Avenue West<br>Suite 400, Fenwick Bay, ON,<br>Canada, K0A 0A0</span>
      </li>
    </ul>
    <div class="bottom-band">
      <span class="website">www.merideldesk-example.com</span>
    </div>
  </section>

</body>
</html>
```